Not-for-profit Community Law Business Card

Not-for-Profit community law firm are looking for new business card design to accompany a new logo.
The cards are to assist the organisation in reaching their strategic objective of generating greater networking amongst the community; specifically with other service providers, clients, and community influencers.
It should stand out. Be professional, strong, creative, clear in detail. The logo should be a major feature of the design.
Updates

Hi All,

Thank you for the submissions so far. I have uploaded the logo and colour details again, as requested. If you have any further issues downloading them or need a different format please contact me on rosa_pellin@vtq.example.au

Kind regards,

Industry/Entity Type

Law Firm

Requirements
Must have
• Logo (attached)
Person's name
Position
Phone
Fax
Email
PO Box address
Website
Colours from the logo.

```html
<!DOCTYPE html>
<html lang="en">
<head>
<meta charset="utf-8">
<title>Bayside Community Legal Centre – Business Card</title>
<link rel="stylesheet" href="https://fonts.googleapis.com/css2?family=Didact+Gothic&display=swap">
<style>
  :root {
    --backdrop: #e9e6e1;
    --card: #fbfbfb;
    --ink: #2b2b2b;
    --navy: #2c2f8f;
    --blue: #2a7fc9;
    --beam: #d3dae3;
  }
  * { box-sizing: border-box; margin: 0; padding: 0; }
  html, body { width: 1200px; height: 900px; overflow: hidden; }
  body {
    background: var(--backdrop);
    font-family: "Didact Gothic", "Century Gothic", sans-serif;
    color: var(--ink);
    position: relative;
  }
  .card {
    position: absolute;
    width: 700px;
    height: 400px;
    background: var(--card);
    box-shadow: 0 6px 18px rgba(0,0,0,0.18);
    overflow: hidden;
  }
  .card--back { left: 330px; top: 40px; }
  .card--front { left: 170px; top: 460px; }

  .back-beam {
    position: absolute;
    left: 0; top: 0;
    width: 700px; height: 400px;
  }
  .back-name {
    position: absolute;
    right: 48px; bottom: 70px;
    text-align: right;
    color: var(--blue);
    font-size: 34px;
    line-height: 1.1;
    letter-spacing: 1px;
  }
  .back-name span { display: block; font-size: 20px; }

  .front-brand {
    position: absolute;
    right: 44px; top: 40px;
    display: flex;
    align-items: center;
    gap: 14px;
    color: var(--blue);
  }
  .brand-dot {
    width: 44px; height: 44px;
    border-radius: 50%;
    background: var(--blue);
    flex: none;
  }
  .brand-name { font-size: 28px; line-height: 1.1; letter-spacing: 1px; }
  .brand-name span { display: block; font-size: 17px; text-align: right; }

  .person {
    position: absolute;
    left: 50px; top: 150px;
    font-size: 28px;
    letter-spacing: 1px;
    text-transform: uppercase;
  }
  .person .role { font-size: 19px; }
  .contact {
    position: absolute;
    left: 50px; top: 212px;
    font-size: 18px;
    line-height: 1.35;
  }
  .contact b { color: var(--navy); font-weight: 400; margin-right: 4px; }
  .contact .web { color: var(--navy); margin-top: 10px; letter-spacing: 0.5px; }
  .contact .address { margin-top: 10px; font-size: 19px; }
</style>
</head>
<body>
  <section class="card card--back">
    <svg class="back-beam" viewBox="0 0 700 400" aria-hidden="true">
      <polygon points="150,150 700,0 700,55 150,190" fill="var(--beam)"/>
    </svg>
    <div class="back-name">Bayside Community<span>Legal Centre Inc.</span></div>
  </section>

  <section class="card card--front">
    <div class="front-brand">
      <div class="brand-dot"></div>
      <div class="brand-name">Bayside Community<span>Legal Centre Inc.</span></div>
    </div>
    <h1 class="person">Marla Quinn <span class="role">| Manager</span></h1>
    <div class="contact">
      <p><b>t</b>555.018.0358 <b>f</b>555.018.0147</p>
      <p><b>e</b>mquinn@baysidecommunity.example</p>
      <p class="web">www.baysidecommunity.example</p>
      <p class="address">PO Box 4120, Harbour Rd, Port Ellis 2301</p>
    </div>
  </section>
</body>
</html>
```